Broschüren-Design für Produzent von hochwertigen Verpackungs- und Präsentationslösungen
Zielgruppe
Wir produzieren hochwertige Verpackungs- und Präsentationslösungen.
Unsere Zielgruppe sind Firmen, welche kreative Premium-Packaging benötigt.
Aufgabenstellung
- Format: A4 hoch
- Umfang: 6 Seiten
- Falzart: Wickelfalz
- Design muss sehr hochwertig sein. Passend zu unseren Produktion (siehe Bilder)
- Wir möchten mit diesem Falzprospekt eine Übersicht über unsere Produkte generieren.
- Die Produkte sind bereits schon hochwertig fotografiert und müssen in einem anspruchsvollen Design in Szene gesetzt werden.
- Der Prospekt sollte die Kunden emotional berühren.
- Auf der Titelseite werden wir den Titel «High Performance Packaging» mit Folien prägen
- Seitenaufbau gemäss meiner Visualisierung (im Anhang)
- Bei jeder Produktkategorie möchte ich ein Grosses Übersichtsbild zusammen mit einem kurzen Text.
Ergänzend können noch weitere (passende) Bilder der jeweiligen Kategorie abgebildet werden.
Im Anhang finden Sie:
- Visualisierung des zu gestaltenden Prospekt
- Werbeflyer (zur Ansicht/Inspiration). In etwa so stellen wir uns das Design/Tonalität vor.
- Weitere passende Produktbilder können vorerst auf der Webseite unseres Produktionspartner (www.bogenhaus.de) entnommen werden.

```html
<!DOCTYPE html>
<html lang="de">
<head>
<meta charset="utf-8">
<title>High Performance Packaging – Titelseite</title>
<link rel="stylesheet" href="https://fonts.googleapis.com/css2?family=Montserrat:wght@600;700&family=Poppins:wght@300;400&display=swap">
<style>
  :root {
    --stage: #e9e9e9;
    --navy: #363d4c;
    --navy-light: #444c5c;
    --navy-dark: #2b313e;
    --copper: #c27b55;
    --copper-light: #d99a74;
    --copper-dark: #9c5a3a;
    --ink-light: #c9ccd4;
  }
  * { margin: 0; padding: 0; box-sizing: border-box; }
  html, body {
    width: 1200px;
    height: 804px;
    overflow: hidden;
    background: var(--stage);
  }
  .stage {
    position: relative;
    width: 1200px;
    height: 804px;
    display: flex;
    align-items: center;
    justify-content: center;
  }
  .cover {
    position: relative;
    width: 510px;
    height: 722px;
    overflow: hidden;
    background:
      linear-gradient(150deg, var(--navy-light) 0%, var(--navy) 45%, var(--navy-dark) 100%);
  }
  .cover-title {
    position: absolute;
    left: 72px;
    top: 190px;
    font-family: "Montserrat", sans-serif;
    font-weight: 700;
    text-transform: uppercase;
    line-height: 0.82;
    background: linear-gradient(100deg, var(--copper-dark) 0%, var(--copper) 35%, var(--copper-light) 55%, var(--copper) 75%, var(--copper-dark) 100%);
    -webkit-background-clip: text;
    background-clip: text;
    color: transparent;
  }
  .cover-title span { display: block; }
  .cover-title .title-high {
    font-size: 56px;
    letter-spacing: 1px;
    margin-left: 8px;
  }
  .cover-title .title-performance {
    font-size: 29px;
    font-weight: 600;
    letter-spacing: 0.5px;
  }
  .cover-title .title-packaging {
    font-size: 56px;
    letter-spacing: 1px;
    margin-left: 48px;
  }
  .cover-photo {
    position: absolute;
    left: 150px;
    right: 0;
    top: 340px;
    height: 170px;
    background:
      radial-gradient(ellipse at 28% 55%, rgba(194,123,85,0.55) 0%, rgba(194,123,85,0) 45%),
      radial-gradient(ellipse at 70% 60%, rgba(150,160,180,0.35) 0%, rgba(150,160,180,0) 50%),
      linear-gradient(180deg, rgba(54,61,76,0) 0%, rgba(38,43,54,0.6) 100%);
  }
  .cover-brand {
    position: absolute;
    left: 0;
    right: 0;
    top: 588px;
    text-align: center;
    font-family: "Poppins", sans-serif;
    font-weight: 400;
    font-size: 13px;
    letter-spacing: 3px;
    text-transform: uppercase;
    color: #ffffff;
  }
  .cover-tagline {
    position: absolute;
    left: 0;
    right: 0;
    bottom: 48px;
    text-align: center;
    font-family: "Poppins", sans-serif;
    font-weight: 300;
    font-size: 12.5px;
    letter-spacing: 0.6px;
    color: var(--ink-light);
  }
</style>
</head>
<body>
  <main class="stage">
    <section class="cover">
      <h1 class="cover-title">
        <span class="title-high">High</span>
        <span class="title-performance">Performance</span>
        <span class="title-packaging">Packaging</span>
      </h1>
      <div class="cover-photo" role="img" aria-label="Produktfoto: kupferfarbene Schiebebox, graue Schubladenbox mit Kupfergriffen und geöffnetes Etui auf dunklem Grund"></div>
      <div class="cover-brand">Kastenwerk</div>
      <p class="cover-tagline">Exklusive Verpackungs- und Präsentationslösungen</p>
    </section>
  </main>
</body>
</html>
```